Dietitian needs awesome business card

I need a contemporary design that's eye catching but professional.
My card is to given to doctors, specialists and patients alike.
I manage patients with chronic diseases
I have uploaded my logo and current business card, I would also like the other Registered Clinical Nutritionist logo incorporated into the design

Target Market(s)

Doctors, specialists and patients

Industry/Entity Type

Healthcare

Contact Information for Business Card

www.brindlecovenutrition.com.au
Ph: 0427 516 903
Fax: 6482 7315
email: marcus.k.wellfare@quorvamail.com
Space on the back of the card with: Appointment date, Appointment time and appointment location

Font styles to use
Serif

Colors
fbee3e
876aae
ffc214

Requirements
Must have
• My Logo
• Registered Clinical Nutritionist Logo
• My 4 locations - Fernhollow Medical Centre, North Kelby Health, Ashcourt Medical, Pinebrook Doctors Surgery
Nice to have
• I like the colours in my current business card

```html
<!DOCTYPE html>
<html lang="en">
<head>
<meta charset="utf-8">
<title>Brindle Cove Nutrition &amp; Dietetics – Business Card</title>
<link rel="stylesheet" href="https://fonts.googleapis.com/css2?family=Raleway:wght@400;500;700&family=Lora:ital@1&display=swap">
<style>
  :root {
    --bg: #e6e6e8;
    --card: #fbfbfb;
    --ink: #1b1b1b;
    --band: #1a1a1a;
    --green: #9ccb2e;
    --blue: #1b64b8;
    --navy: #1e3a8c;
    --orange: #f47a20;
    --muted: #8a8a8a;
  }
  * { box-sizing: border-box; margin: 0; padding: 0; }
  html, body { width: 1200px; height: 800px; overflow: hidden; }
  body {
    background: var(--bg);
    font-family: "Raleway", sans-serif;
    color: var(--ink);
    position: relative;
  }
  .card {
    position: absolute;
    top: 245px;
    width: 540px;
    height: 310px;
    background: var(--card);
    border-radius: 16px;
    overflow: hidden;
    box-shadow: 0 6px 18px rgba(0,0,0,.18);
  }
  .card--front { left: 40px; }
  .card--back { left: 620px; }
  .card__bands { position: absolute; inset: 0; }

  /* front */
  .contact { position: absolute; left: 36px; top: 34px; }
  .contact__name { font-size: 21px; color: var(--green); letter-spacing: .2px; }
  .contact__name b { font-weight: 700; }
  .contact__name span { font-weight: 400; }
  .contact__role { font-size: 13px; margin-top: 6px; font-weight: 500; }
  .contact__role i { font-style: normal; color: var(--green); margin: 0 6px; }
  .contact__line { display: flex; align-items: center; gap: 8px; font-size: 12.5px; margin-top: 7px; }
  .contact__icon { width: 11px; height: 11px; }

  .brand { position: absolute; display: flex; align-items: center; gap: 8px; }
  .brand__dot { width: 26px; height: 26px; border-radius: 50%; background: var(--green); flex: none; }
  .brand__name { font-size: 15px; font-weight: 500; color: var(--blue); line-height: 1.15; }
  .brand--front { left: 230px; top: 252px; }
  .brand--front .brand__name { color: #ffffff; }
  .badge { position: absolute; left: 440px; top: 246px; width: 76px; height: 48px; background: var(--orange); }

  /* back */
  .brand--back { left: 34px; top: 34px; }
  .brand--back .brand__name { font-size: 18px; }
  .appointment { position: absolute; left: 150px; top: 118px; width: 310px; }
  .appointment__title { font-size: 22px; color: var(--green); font-weight: 400; margin-bottom: 10px; letter-spacing: .5px; }
  .field { display: flex; align-items: flex-end; gap: 8px; font-size: 12.5px; height: 24px; }
  .field__label { flex: none; }
  .field__line { flex: 1; border-bottom: 1px solid var(--green); height: 1px; margin-bottom: 3px; }
  .quote {
    position: absolute; right: 26px; top: 104px; width: 92px;
    font-family: "Lora", serif; font-style: italic; font-size: 11px;
    color: var(--muted); line-height: 1.35; text-align: left;
  }
</style>
</head>
<body>

<section class="card card--front" aria-label="Card front">
  <svg class="card__bands" viewBox="0 0 540 310" aria-hidden="true">
    <rect x="0" y="298" width="540" height="12" fill="var(--band)"/>
    <polygon points="0,262 200,262 190,292 0,292" fill="var(--band)"/>
    <polygon points="62,262 122,262 112,292 52,292" fill="var(--green)"/>
    <polygon points="122,262 182,262 172,292 112,292" fill="var(--blue)"/>
    <polygon points="210,230 540,230 540,310 180,310" fill="var(--band)"/>
  </svg>

  <div class="contact">
    <p class="contact__name"><b>Marcus</b><span>Wellfare</span></p>
    <p class="contact__role">Registered Clinical Nutritionist<i>/</i>Nutritionist and Chef</p>
    <p class="contact__line">
      <svg class="contact__icon" viewBox="0 0 12 12" aria-hidden="true"><rect width="12" height="12" rx="2" fill="var(--green)"/><path d="M3.5 3h1.6l.6 1.6-.9.7a5 5 0 0 0 2 2l.7-.9 1.6.6V8.6A.9.9 0 0 1 8 9.5 5.8 5.8 0 0 1 2.5 4a.9.9 0 0 1 1-1z" fill="#fff"/></svg>
      0427 516 903
    </p>
    <p class="contact__line">
      <svg class="contact__icon" viewBox="0 0 12 12" aria-hidden="true"><rect width="12" height="12" rx="2" fill="var(--green)"/><rect x="2.5" y="3.5" width="7" height="5" fill="none" stroke="#fff" stroke-width="1"/><path d="M2.5 3.5 6 6.3 9.5 3.5" fill="none" stroke="#fff" stroke-width="1"/></svg>
      marcus.k.wellfare@quorvamail.com
    </p>
  </div>

  <div class="brand brand--front">
    <span class="brand__dot"></span>
    <span class="brand__name">Brindle Cove<br>Nutrition &amp; Dietetics</span>
  </div>
  <div class="badge" role="img" aria-label="Professional accreditation badge"></div>
</section>

<section class="card card--back" aria-label="Card back">
  <svg class="card__bands" viewBox="0 0 540 310" aria-hidden="true">
    <rect x="0" y="296" width="540" height="14" fill="var(--band)"/>
    <polygon points="0,262 200,262 190,292 0,292" fill="var(--band)"/>
    <polygon points="62,262 122,262 112,292 52,292" fill="var(--green)"/>
    <polygon points="122,262 182,262 172,292 112,292" fill="var(--blue)"/>
    <polygon points="200,240 460,240 480,310 180,310" fill="var(--band)"/>
  </svg>

  <div class="brand brand--back">
    <span class="brand__dot"></span>
    <span class="brand__name">Brindle Cove<br>Nutrition &amp; Dietetics</span>
  </div>

  <div class="appointment">
    <h2 class="appointment__title">Appointment</h2>
    <div class="field"><span class="field__label">Name</span><span class="field__line"></span></div>
    <div class="field"><span class="field__label">Date</span><span class="field__line"></span><span class="field__label">Time</span><span class="field__line"></span></div>
    <div class="field"><span class="field__label">Location</span><span class="field__line"></span></div>
  </div>

  <p class="quote">“Let food be thy medicine and medicine be thy food”</p>
</section>

</body>
</html>
```